Author needs cover design for health related book

I need the front cover designed for an upcoming book. I want a cover that will stand out when viewed in a thumbnail on sites such as Brindleway. I'm open to the color scheme. The cover design should convey hopeful, uplifting energy, trust, and confidence. Nothing cute or frilly, please. The book is written for newly diagnosed cancer patients. The book title is: They Told Me Today, So What Next? Subtitle: Bravely Facing Cancer Through Worry, Confusion and Dread
Author: Darlisse Hovard
I'm not window shopping. I will definitely pick one of the submitted designs.
Target Market(s)
Newly diagnosed cancer patients
Industry/Entity Type
Health Care
Look and feel
Each slider illustrates characteristics of the customer's brand and the style your logo design should communicate.

```html
<!DOCTYPE html>
<html lang="en">
<head>
<meta charset="utf-8">
<title>They Told Me Today, So What Next? — Book Cover</title>
<link rel="stylesheet" href="https://fonts.googleapis.com/css2?family=Noto+Serif:ital,wght@0,400;0,500;1,400;1,500&display=swap">
<style>
  :root {
    --paper-light: #eeedeb;
    --paper-mid: #e2e0dd;
    --paper-dark: #d3d0cc;
    --purple-bright: #9c5fe0;
    --purple-deep: #6a3f86;
    --ink: #1d1b1c;
    --skin-light: #f1c8a6;
    --skin-mid: #d9956a;
    --skin-shadow: #b8724b;
  }
  * { margin: 0; padding: 0; box-sizing: border-box; }
  html, body {
    width: 1188px;
    height: 1200px;
    overflow: hidden;
    background: #ffffff;
  }
  .cover {
    position: relative;
    width: 1188px;
    height: 1200px;
    overflow: hidden;
    background:
      linear-gradient(160deg, var(--paper-dark) 0%, var(--paper-mid) 35%, var(--paper-light) 70%, var(--paper-mid) 100%);
    font-family: "Noto Serif", Georgia, serif;
  }
  .title-block {
    position: absolute;
    top: 80px;
    right: 70px;
    text-align: right;
    line-height: 1;
    z-index: 2;
  }
  .title-lead {
    display: block;
    font-size: 96px;
    font-weight: 500;
    color: var(--purple-bright);
    letter-spacing: -1px;
  }
  .title-main {
    display: block;
    font-size: 190px;
    font-weight: 500;
    color: var(--purple-bright);
    letter-spacing: -4px;
    margin-top: -6px;
  }
  .title-question {
    display: block;
    font-size: 132px;
    font-weight: 500;
    color: var(--purple-deep);
    letter-spacing: -2px;
    margin-top: 10px;
  }
  .subtitle {
    position: absolute;
    top: 600px;
    right: 80px;
    text-align: right;
    font-size: 46px;
    font-weight: 400;
    line-height: 1.2;
    color: var(--ink);
    z-index: 2;
  }
  .hands-photo {
    position: absolute;
    left: 0;
    top: 790px;
    width: 1188px;
    height: 270px;
    z-index: 1;
  }
  .author {
    position: absolute;
    left: 300px;
    bottom: 50px;
    font-size: 66px;
    font-weight: 500;
    color: var(--purple-bright);
    letter-spacing: -0.5px;
    z-index: 2;
  }
</style>
</head>
<body>
  <main class="cover">
    <h1 class="title-block">
      <span class="title-lead">They Told Me</span>
      <span class="title-main">Today,</span>
      <span class="title-question">So What Next?</span>
    </h1>

    <p class="subtitle">Bravely Facing Cancer<br>Through Worry,<br>Confusion and Dread</p>

    <svg class="hands-photo" viewBox="0 0 1188 270" preserveAspectRatio="none" role="img" aria-label="Photograph of two hands reaching toward each other, one gently holding the other's fingers">
      <defs>
        <linearGradient id="skinTone" x1="0" y1="1" x2="1" y2="0">
          <stop offset="0" stop-color="#f1c8a6" stop-opacity="0.85"/>
          <stop offset="0.5" stop-color="#d9956a" stop-opacity="0.75"/>
          <stop offset="1" stop-color="#b8724b" stop-opacity="0.7"/>
        </linearGradient>
      </defs>
      <path d="M0 270 L0 245 C250 200 470 160 650 120 C820 75 990 30 1188 0 L1188 110 C1000 170 820 230 620 255 C420 268 200 270 0 270 Z" fill="url(#skinTone)"/>
    </svg>

    <p class="author">Darlisse Hovard</p>
  </main>
</body>
</html>
```